A hand soap seller needs a premium label for a new product

We need a premium label for a bottle of soap. We want to write on it:
VANTROSELLA (Name)
Hypoallergenic and antibacterial hand soap
350 ml e / 11.8 fl oz (volume, http://pimaxo.ru/7K3RtWbqmeL519)
Saint Petersburg - Russia / www.vantrosella.ru
We want to see the face of a hippopotamus in the design. Use only black and white and green for accents (the color of grass). Examples of a hippopotamus are shown in the photo. Our soap is hypoallergenic. Ideal for both children and adults. Therefore, the label should appeal to adults and children.
The bottle will be white, and the soap dispenser will be black.
So I'm attaching an example of a soap design that we liked
Label size: height-78 mm, width-102 mm !!!

Target Market(s)

Mothers and children

Industry/Entity Type

Hand soap

Font styles to use
Serif

Colors

Designer to choose only greyscale colors for use in the design.

Requirements
Must have
• The face of a hippopotamus emerging from the grass, Black and white palette with elements of green (grass color)
Nice to have
• The face of a hippopotamus emerging from the grass
Should not have
• Different colors

```html
<!DOCTYPE html>
<html lang="en">
<head>
<meta charset="utf-8">
<title>Vantrosella Hand Soap Label</title>
<link rel="stylesheet" href="https://fonts.googleapis.com/css2?family=Comfortaa:wght@400;600&family=Montserrat:wght@300;700&display=swap">
<style>
  :root {
    --ink: #000000;
    --paper: #ffffff;
    --grass: #1f9a4a;
    --pattern-light: #5a5a5a;
    --pattern-dark: #1c1c1c;
    --illustration-tone: #e4e4e4;
  }
  html, body {
    margin: 0;
    width: 1200px;
    height: 1200px;
    overflow: hidden;
    background: var(--paper);
  }
  .canvas {
    position: relative;
    width: 1200px;
    height: 1200px;
  }
  .label {
    position: absolute;
    left: 100px;
    top: 217px;
    width: 1000px;
    height: 766px;
  }
  .brand-bold { font-family: "Montserrat", sans-serif; font-weight: 700; fill: var(--paper); }
  .brand-light { font-family: "Montserrat", sans-serif; font-weight: 300; fill: var(--paper); }
  .product-line { font-family: "Comfortaa", sans-serif; font-weight: 400; font-size: 28px; fill: var(--ink); }
  .product-name { font-family: "Comfortaa", sans-serif; font-weight: 600; font-size: 28px; fill: var(--grass); letter-spacing: 1px; }
  .volume { font-family: "Comfortaa", sans-serif; font-weight: 400; font-size: 24px; fill: var(--paper); }
  .origin { font-family: "Comfortaa", sans-serif; font-weight: 400; font-size: 22px; fill: var(--ink); }
  .website { font-family: "Comfortaa", sans-serif; font-weight: 400; font-size: 22px; fill: var(--grass); }
</style>
</head>
<body>
<div class="canvas">
  <svg class="label" viewBox="0 0 985 754" xmlns="http://www.w3.org/2000/svg">
    <defs>
      <clipPath id="pattern-area">
        <path d="M0,408 C70,430 110,465 175,465 C260,465 320,392 410,392 C500,392 530,476 600,476 C690,476 720,398 800,398 C880,398 930,452 985,472 L985,0 L0,0 Z"/>
      </clipPath>
      <linearGradient id="pattern-tone" x1="0" y1="0" x2="1" y2="1">
        <stop offset="0" stop-color="var(--pattern-light)"/>
        <stop offset="0.5" stop-color="var(--pattern-dark)"/>
        <stop offset="1" stop-color="var(--pattern-light)"/>
      </linearGradient>
    </defs>

    <rect class="label-ground" x="0" y="0" width="985" height="754" fill="var(--paper)"/>

    <!-- black header with wavy lower edge -->
    <path class="header-band" d="M0,410 C70,440 110,485 175,485 C260,485 320,395 410,395 C500,395 530,480 600,480 C690,480 720,400 800,400 C880,400 930,455 985,475 L985,0 L0,0 Z" fill="var(--ink)"/>

    <g clip-path="url(#pattern-area)">
      <rect class="pattern-left" x="0" y="0" width="357" height="500" fill="url(#pattern-tone)" role="img" aria-label="Repeating pattern of hand-drawn hippo faces with flowers, white line art on black"/>
      <rect class="pattern-right" x="632" y="0" width="353" height="500" fill="url(#pattern-tone)" role="img" aria-label="Repeating pattern of hand-drawn hippo faces with flowers, white line art on black"/>
    </g>

    <!-- grass accent line along the wave -->
    <path class="grass-line" d="M0,408 C70,430 110,465 175,465 C260,465 320,392 410,392 C500,392 530,476 600,476 C690,476 720,398 800,398 C880,398 930,452 985,472" fill="none" stroke="var(--grass)" stroke-width="2.5"/>

    <!-- name frame -->
    <path class="name-frame" d="M395,0 L395,359 C470,362 540,390 592,436 L592,0" fill="none" stroke="var(--paper)" stroke-width="2"/>

    <text class="brand-bold" x="410" y="284" font-size="46" textLength="168" lengthAdjust="spacingAndGlyphs">VANTRO</text>
    <text class="brand-light" x="410" y="333" font-size="46" textLength="168" lengthAdjust="spacingAndGlyphs">SELLA</text>

    <text class="product-line" x="357" y="516">Hypoallergenic</text>
    <text class="product-line" x="357" y="552">and antibacterial</text>
    <text class="product-name" x="357" y="589">HAND SOAP</text>

    <!-- volume block -->
    <path class="volume-block" d="M355,618 C400,612 450,612 500,635 C545,660 570,690 629,697 L629,754 L355,754 Z" fill="var(--ink)"/>
    <rect class="hippo-mark" x="542" y="627" width="86" height="70" rx="12" fill="var(--illustration-tone)" role="img" aria-label="Small line drawing of a hippo peeking out with a flower"/>
    <text class="volume" x="375" y="732">350 ml ℮ / 11.8 fl oz</text>

    <text class="origin" x="715" y="675">Saint Petersburg</text>
    <text class="origin" x="715" y="704">Russia</text>
    <text class="website" x="715" y="732">www.vantrosella.ru</text>

    <rect class="label-edge" x="1" y="1" width="983" height="752" fill="none" stroke="var(--ink)" stroke-width="2"/>
  </svg>
</div>
</body>
</html>
```